Forward thinking startup needs business cards

We are a new company entering the fall protection market and we need business cards. We provide equipment and supplies to a very large industry, and we aim to catch the attention of the end-user; not just the distributors. Please browse brovanteq.com for a better feel of our initial branding. The hog images are not required, but are here for inspiration. Also, they should not be prominent in the design as much as an accent. Many of our customers will be very high-end, so this should be considered as well.

Target Market(s)

Buyers for the safety industry. Some accounts will be very large, but most of these people are very down-to-earth.

Industry/Entity Type

Business

Contact Information for Business Card

Name and title
phone: 1-800-563-2814
fax: 740-318-5096
web: www.brovanteq.com
address: 712 Quarrybend Lane, Waterford, OH 45786 USA
room for cell number, direct office phone number, extension, and email

Font styles to use
Serif
Sans Serif

Colors
f37122
ffffff

Requirements
Must have
• Should be very clean and easy to read. We typically use orange and grey in our color schemes - #ef7c2d and #424242
Nice to have
• It would be nice to have room somewhere to incorporate some of the other logos from our family of companies. At the same time, it should not look weird if they aren't included.

```html
<!DOCTYPE html>
<html lang="en">
<head>
<meta charset="utf-8">
<title>Brovanteq Business Card</title>
<link rel="stylesheet" href="https://fonts.googleapis.com/css2?family=Open+Sans:wght@400;700;800&family=Noto+Serif:wght@400;700&display=swap">
<style>
  :root {
    --orange: #ef7c2d;
    --grey: #424242;
    --white: #ffffff;
    --backdrop: #e9e7e4;
  }
  * { margin: 0; padding: 0; box-sizing: border-box; }
  html, body { width: 1200px; height: 900px; overflow: hidden; }
  body {
    background: var(--backdrop);
    font-family: "Open Sans", Arial, sans-serif;
    position: relative;
  }
  .card {
    position: absolute;
    left: 250px;
    width: 700px;
    height: 400px;
    overflow: hidden;
    box-shadow: 0 6px 18px rgba(0,0,0,0.18);
  }
  .card-front { top: 35px; background: var(--orange); }
  .card-back { top: 465px; background: var(--white); }

  .front-wordmark {
    position: absolute;
    left: 0; right: 0; top: 150px;
    text-align: center;
    font-weight: 800;
    font-size: 78px;
    letter-spacing: 1px;
    color: var(--white);
  }

  .back-shape { position: absolute; inset: 0; }

  .back-wordmark {
    position: absolute;
    left: 40px; top: 170px;
    font-weight: 800;
    font-size: 46px;
    color: var(--grey);
  }

  .holder {
    position: absolute;
    left: 495px; top: 118px;
    color: var(--white);
    font-family: "Noto Serif", Georgia, serif;
    text-align: center;
  }
  .holder-name { font-weight: 700; font-size: 21px; letter-spacing: 0.5px; }
  .holder-title { font-size: 13px; }

  .contact-list {
    position: absolute;
    left: 300px; top: 258px;
    list-style: none;
    color: var(--white);
    font-size: 19px;
    line-height: 29px;
  }
  .contact-list li { display: flex; align-items: center; gap: 12px; }
  .contact-icon {
    width: 22px; height: 22px;
    background: var(--white);
    border-radius: 5px;
    display: flex; align-items: center; justify-content: center;
  }
  .contact-icon svg { width: 14px; height: 14px; }
</style>
</head>
<body>
  <section class="card card-front" aria-label="Card front">
    <div class="front-wordmark">Brovanteq</div>
  </section>

  <section class="card card-back" aria-label="Card back">
    <svg class="back-shape" viewBox="0 0 700 400" width="700" height="400" aria-hidden="true">
      <polygon points="172,400 452,0 700,102 700,400" fill="var(--grey)"/>
      <polygon points="192,400 455,22 700,124 700,400" fill="var(--orange)"/>
    </svg>

    <div class="back-wordmark">Brovanteq</div>

    <div class="holder">
      <div class="holder-name">JOHN SMITH</div>
      <div class="holder-title">Managing Director</div>
    </div>

    <ul class="contact-list">
      <li>
        <span class="contact-icon">
          <svg viewBox="0 0 14 14"><rect x="2" y="5" width="10" height="7" rx="1.5" fill="var(--orange)"/><path d="M1 5 Q7 0 13 5" stroke="var(--orange)" stroke-width="2" fill="none"/></svg>
        </span>123.456.7890
      </li>
      <li>
        <span class="contact-icon">
          <svg viewBox="0 0 14 14"><path d="M3 1 L6 4 L4.5 6 Q6 9 8 9.5 L10 8 L13 11 L11 13 Q4 12 1 3 Z" fill="var(--orange)"/></svg>
        </span>123.456.7890
      </li>
      <li>
        <span class="contact-icon">
          <svg viewBox="0 0 14 14"><rect x="1" y="3" width="12" height="8" rx="1" fill="var(--orange)"/><path d="M1.5 3.5 L7 8 L12.5 3.5" stroke="var(--white)" stroke-width="1.2" fill="none"/></svg>
        </span>info@youremail.com
      </li>
      <li>
        <span class="contact-icon">
          <svg viewBox="0 0 14 14"><rect x="4.5" y="1" width="5" height="6.5" rx="2.5" stroke="var(--orange)" stroke-width="1.6" fill="none"/><rect x="4.5" y="6.5" width="5" height="6.5" rx="2.5" stroke="var(--orange)" stroke-width="1.6" fill="none"/></svg>
        </span>www.yourweb.com
      </li>
    </ul>
  </section>
</body>
</html>
```